Cupcakes blog redesign - cartoon/illustrated style

I need to redesign my food blog muffinmeadow.net.

I really like the current blog design but I want to change Pressleaf theme to responsive and I want to refresh the look of the blog.

Blog design must be in the same style (cartoon, illustrated). The whole idea should be the same as old blog! The header illustration is some kind of garden full of cupcakes. All other elements (left sidebar menu, right sidebar widgets and footer elements) should be in that (garden of cupcakes) style.

The color sheme should be similar to old design. I really like pink, green and light blue color! The content background color must be white.
Only element that must be the same with old site is cupcakes thumbnail images (image 1 in attachment).
Feel fre to change all other elements design .

You can use illustration from http://artbazaarhub.net/search?utf8=%E2%9C%93&term=cupcakes. I will buy these elements later!

You can find all technical details (dimensions,elements...) in the attachment.

This is the list of sites I really like:

1. I adore header of this site - http://www.runbyquick.com/
2. I adore header of this site - http://ful.crumstudio.com/
3. Big site title and overal design - http://morrowtotslab.com/
4. Header - http://ful.crumstudio.com/
5. Footer style :) - http://www.ravolitek.com/
6. Color sheme - http://plumbowlery.com/
7. Color sheme - http://www.hobartilda.com/
8. Color sheme - http://www.gwenbakesdaily.com/

Feel free to contact me for more information.

Good luck

Here is couple illustration example I really like. Of course it should be in Muffin Meadow style:

1. http://pixelbidhall.com/web-design/contests/create-best-site-kids-world-267986/entries/29767275
2. http://pixelbidhall.com/web-design/contests/create-best-site-kids-world-267986/entries/89
3. http://skinforge.com/demo/wp/tadpo-lawn/
4. http://www.blorpcritters.com/login/forums

```html
<!DOCTYPE html>
<html lang="en">
<head>
<meta charset="utf-8">
<title>Muffin Meadow</title>
<link href="https://fonts.googleapis.com/css2?family=Courgette&family=Open+Sans:ital,wght@0,400;0,600;1,400&display=swap" rel="stylesheet">
<style>
:root{
  --pink:#f0727f;
  --pink-soft:#f7a3ab;
  --sky-top:#8ccbee;
  --sky-bottom:#dff1fb;
  --blue-soft:#c6ecf8;
  --blue-btn:#5cc6ec;
  --grass-top:#9fdc5b;
  --grass-bottom:#5aa82c;
  --ink:#222;
  --text:#444;
  --muted:#888;
  --gray-row:#d9d9d9;
  --white:#fff;
}
*{box-sizing:border-box;margin:0;padding:0}
html,body{width:1200px;height:1124px;overflow:hidden}
body{position:relative;font-family:"Open Sans",Arial,sans-serif;color:var(--text);
  background:linear-gradient(180deg,var(--sky-top) 0%,var(--sky-bottom) 70%,#eaf7fd 100%)}
.abs{position:absolute}
.art{position:absolute}
.hills{left:0;top:840px;width:1200px;height:284px;
  background:linear-gradient(180deg,var(--grass-top),var(--grass-bottom));
  border-radius:50% 50% 0 0/60px 60px 0 0}
.header-kid-left{left:245px;top:0;width:160px;height:140px;border-radius:40px;background:linear-gradient(160deg,#f4c35a,#e8663e)}
.header-cupcakes{left:515px;top:82px;width:170px;height:58px;border-radius:30px 30px 8px 8px;background:linear-gradient(90deg,#f7e0c6,#d4a77e,#f59fb0)}
.header-kid-right{left:770px;top:0;width:190px;height:140px;border-radius:40px;background:linear-gradient(160deg,#f2b4c6,#3e6fb0)}
.fireworks{left:960px;top:10px;width:170px;height:320px;border-radius:60px;background:linear-gradient(180deg,rgba(255,255,255,.35),rgba(244,128,170,.25))}
.brand{left:400px;top:26px;width:400px;text-align:center;font-family:"Courgette",cursive;font-size:40px;color:var(--pink);line-height:1}
.brand .dot{display:inline-block;width:26px;height:26px;border-radius:50%;background:var(--pink-soft);vertical-align:middle;margin-right:12px}
.nav{left:260px;top:137px;width:680px;height:40px;background:var(--white);border-radius:6px 10px 4px 8px;display:flex;align-items:center;padding-left:40px}
.nav a{font-family:"Courgette",cursive;font-size:15px;color:var(--ink);text-decoration:none}
.nav .sep{width:16px;height:16px;border-radius:50%;background:#6b4a3a;margin:0 14px}
.nav .search{margin-left:auto;margin-right:14px;display:flex}
.nav .search span{width:118px;height:24px;background:#d5d5d5;font-size:10px;color:#666;padding:5px 8px}
.nav .search b{width:36px;height:24px;background:var(--blue-btn);position:relative}
.search b::after{content:"";position:absolute;left:12px;top:5px;width:9px;height:9px;border:2px solid #fff;border-radius:50%}
.panel{left:260px;top:187px;width:680px;height:800px;background:var(--white);border-radius:0 0 30px 30px}
.brush{display:block;height:27px;background:var(--pink);border-radius:8px 14px 6px 12px;color:#fff;font-family:"Courgette",cursive;font-size:13px;text-align:center;line-height:27px}
.left{left:271px;top:203px;width:160px}
.sub{list-style:none}
.sub li{height:24px;line-height:24px;font-family:"Courgette",cursive;font-size:10px;color:#777;background:var(--gray-row);border-bottom:1px solid #fff;padding-left:14px;display:flex;align-items:center}
.sub li::before{content:"";width:8px;height:8px;border-radius:50%;background:#777;margin-right:9px}
.sub li.active{background:var(--blue-soft);color:var(--ink)}
.sub li.active::before{background:#6b4a3a}
.left .brush{margin-top:12px}
.left .badge{margin-top:14px}
.posts{left:443px;top:203px;width:286px}
.post{height:108px}
.post h2{font-family:"Courgette",cursive;font-weight:400;font-size:14.5px;color:var(--ink);line-height:17px}
.meta{font-size:6.5px;color:#555;font-style:italic;margin-top:3px}
.cats{font-size:7px;color:var(--pink);font-style:italic;margin-top:5px}
.cats b{color:#333;font-style:normal}
.excerpt{display:flex;margin-top:5px;position:relative}
.thumb{width:44px;height:44px;flex:none;border-radius:2px;margin-right:8px}
.excerpt p{font-size:7.2px;line-height:10px;color:#555;padding-right:46px}
.more{position:absolute;right:0;bottom:-2px;background:var(--pink);color:#fff;font-size:6.5px;padding:2px 6px;border-radius:2px}
.t1{background:linear-gradient(#f3e4d0,#c9a27c)}
.t2{background:linear-gradient(#f6d9b3,#b7733a)}
.t3{background:linear-gradient(#f1e1cc,#a4653b)}
.t4{background:linear-gradient(#f5f0ee,#e2445a)}
.t5{background:linear-gradient(#c5e6a8,#4e8c3a)}
.t6{background:linear-gradient(#f7e6ee,#6d7f4e)}
.pager{left:443px;top:887px;width:286px;display:flex;gap:6px;font-size:8px;color:#aaa}
.pager span{border:1px solid #ddd;height:22px;line-height:20px;padding:0 5px;text-align:center}
.pager .cur{background:var(--pink-soft);color:#fff;border-color:var(--pink-soft)}
.pager .last{margin-left:auto}
.right{left:737px;top:203px;width:192px}
.right .brush{height:29px;line-height:29px}
.social{background:var(--blue-soft);height:40px;display:flex;justify-content:center;align-items:center;gap:5px}
.social i{width:19px;height:19px;background:var(--blue-btn);border-radius:2px}
.find{background:var(--blue-soft);height:40px;display:flex;justify-content:center;align-items:center}
.find span{width:122px;height:18px;border:1px solid #999;background:#fff;font-size:8px;padding:3px 5px;color:#666}
.find b{width:18px;height:18px;background:var(--pink);position:relative}
.find b::after{content:"";position:absolute;left:5px;top:4px;width:6px;height:6px;border:1.5px solid #fff;border-radius:50%}
.sponsor{background:var(--blue-soft);height:102px;display:flex;padding:8px 6px}
.sponsor .copy{font-family:"Courgette",cursive;font-size:13px;color:#333;line-height:17px;width:80px}
.sponsor .copy small{display:block;font-family:"Open Sans",sans-serif;font-weight:600;font-size:9px;margin-top:6px}
.sponsor .copy small b{font-size:13px}
.sponsor .boxes{flex:1;border-radius:4px;background:linear-gradient(135deg,#eef3f7,#9fb6d6)}
.about-title{font-family:"Courgette",cursive;color:var(--pink);font-size:14px;text-align:center;margin:14px 0 7px}
.about-img{height:80px;background:linear-gradient(135deg,#f5efe6,#7a4a33)}
.about p{font-size:7.2px;line-height:10px;color:#555;margin-top:5px;position:relative}
.about .more{position:static;display:inline-block;float:right;margin-top:2px}
.popular li{list-style:none;display:flex;height:48px}
.popular .pt{width:46px;height:40px;flex:none;margin-right:7px}
.popular h3{font-size:9.2px;font-weight:600;color:#333;line-height:12px}
.popular p{font-size:7.5px;color:#666;margin-top:3px;line-height:10px}
.footer-links{left:257px;top:1098px;font-size:8.5px;color:#222}
.copyright{left:740px;top:1098px;font-size:8px;color:#222}
</style>
</head>
<body>
<div class="art hills" role="img" aria-label="Rolling green hills with cartoon children, a hen with chicks, a squirrel, a tree and a young painter at an easel"></div>
<div class="art fireworks" role="img" aria-label="Cartoon fireworks rockets and bursts in the sky"></div>
<div class="art header-kid-left" role="img" aria-label="Cartoon girl with a basket and a toy rocket"></div>
<div class="art header-cupcakes" role="img" aria-label="Row of smiling cartoon cupcakes"></div>
<div class="art header-kid-right" role="img" aria-label="Gift boxes and a cartoon boy with a hat"></div>

<div class="abs brand"><span class="dot"></span>muffin meadow</div>

<nav class="abs nav">
  <a href="#">Home</a><span class="sep"></span>
  <a href="#">Cupcakes 101</a><span class="sep"></span>
  <a href="#">Muffin Meadow Recipes</a><span class="sep"></span>
  <a href="#">Contact</a>
  <div class="search"><span>Search</span><b></b></div>
</nav>

<div class="abs panel"></div>

<aside class="abs left">
  <span class="brush">Categoty Item</span>
  <ul class="sub">
    <li class="active">Subcategory Item</li>
    <li>Subcategory Item</li>
    <li>Subcategory Item</li>
    <li>Subcategory Item</li>
    <li>Subcategory Item</li>
    <li>Subcategory Item</li>
  </ul>
  <span class="brush">Categoty Item</span>
  <span class="brush" style="margin-top:9px">Categoty Item</span>
  <span class="brush" style="margin-top:9px">Categoty Item</span>
  <span class="brush badge">Grab our badge</span>
</aside>

<main class="abs posts">
  <article class="post">
    <h2>Piña Colada Cupcakes by Velmont Baker</h2>
    <div class="meta">Posted on | March 14, 2014</div>
    <div class="cats"><b>Category:</b> Beer and Liquor cupcakes, Coconut cupcakes, Cupcake recipes</div>
    <div class="excerpt"><div class="thumb t1" role="img" aria-label="Piña colada cupcake"></div>
      <p>It's not even spring and perhaps it's too early for a summer cocktails, but you can enjoy cocktail inspired cupcakes, while waiting for warm weather. Piña Colada cup cakes are pineapple-coconut cupcake with dark rum, topped with coconut cream cheese frosting.</p><span class="more">Read More</span></div>
  </article>
  <article class="post">
    <h2>Piña Colada Cupcakes by Velmont Baker</h2>
    <div class="meta">Posted on | March 14, 2014</div>
    <div class="cats"><b>Category:</b> Beer and Liquor cupcakes, Coconut cupcakes, Cupcake recipes</div>
    <div class="excerpt"><div class="thumb t2" role="img" aria-label="Piña colada cupcake"></div>
      <p>It's not even spring and perhaps it's too early for a summer cocktails, but you can enjoy cocktail inspired cupcakes, while waiting for warm weather. Piña Colada Cupcakes are pineapple-coconut cupcake with dark rum, topped with</p><span class="more">Read More</span></div>
  </article>
  <article class="post" style="height:123px">
    <h2>Apple Cinnamon Pancake Cupcakes with Crispy Bacon Sprinkles</h2>
    <div class="meta">Posted on | March 14, 2014</div>
    <div class="cats"><b>Category:</b> Beer and Liquor cupcakes, Coconut cupcakes, Cupcake recipes</div>
    <div class="excerpt"><div class="thumb t3" role="img" aria-label="Apple cinnamon pancake cupcake"></div>
      <p>It's not even spring and perhaps it's too early for a summer cocktails, but you can enjoy cocktail inspired cupcakes, while waiting for warm weather. Piña Colada cup cakes are pineapple-coconut cupcake with dark rum.</p><span class="more">Read More</span></div>
  </article>
  <article class="post" style="height:113px">
    <h2>Skinny Mini Strawberry Cheesecakes</h2>
    <div class="meta">Posted on | March 13, 2014</div>
    <div class="cats"><b>Category:</b> Beer and Liquor cupcakes, Coconut cupcakes, Cupcake recipes</div>
    <div class="excerpt"><div class="thumb t4" role="img" aria-label="Strawberry cheesecake cupcake"></div>
      <p>Skinny Mini Strawberry Cheesecakes by Sugar and a Grin are rich and creamy dessert although they contain less fat that regular cheesecakes. Using less fat cream cheese and fat free yogurt, these cupcakes are better for you</p><span class="more">Read More</span></div>
  </article>
  <article class="post" style="height:113px">
    <h2>Marbled Rowan's Peanut Butter Cup Cupcakes</h2>
    <div class="meta">Posted on | March 13, 2014</div>
    <div class="cats"><b>Category:</b> Chocolate cupcakes, Cupcake recipes, Peanut butter cupcakes</div>
    <div class="excerpt"><div class="thumb t5" role="img" aria-label="Marbled peanut butter cupcake"></div>
      <p>With these awesome Marbled Rowan's Peanut Butter Cup Cupcakes by A Wafer Called Wish you'll get perfect chocolate peanut butter combo in every bite. The cupcakes are marbled chocolate and peanut butter cake filled with</p><span class="more">Read More</span></div>
  </article>
  <article class="post">
    <h2>Rainbow Poke Cupcakes</h2>
    <div class="meta">Posted on | March 13, 2014</div>
    <div class="cats"><b>Category:</b> Chocolate cupcakes, Cupcake recipes, Peanut butter cupcakes</div>
    <div class="excerpt"><div class="thumb t6" role="img" aria-label="Rainbow poke cupcake"></div>
      <p>Adorable looking Rainbow Poke Cupcakes are great idea for St. Patrics Day treat, or for some kids party. Kids will love this cute dessert, and they could be your little helper in the kitchen while making the cupcakes because the recipe is</p><span class="more">Read More</span></div>
  </article>
</main>

<div class="abs pager">
  <span>Page 1 to 336</span><span class="cur">01</span><span>02</span><span>03</span><span>04</span><span>....</span><span class="last">Last Page</span>
</div>

<aside class="abs right">
  <span class="brush">follow us</span>
  <div class="social"><i></i><i></i><i></i><i></i><i></i><i></i></div>
  <span class="brush" style="margin-top:11px">Find Out Blog</span>
  <div class="find"><span>Search</span><b></b></div>
  <span class="brush" style="margin-top:0">Our Sponsers</span>
  <div class="sponsor">
    <div class="copy">Sell Your Diabetic Test Strips!<small>Up To <b>$40</b> a box</small></div>
    <div class="boxes" role="img" aria-label="Boxes of test strips"></div>
  </div>
  <div class="about">
    <div class="about-title">About Us</div>
    <div class="about-img" role="img" aria-label="Cupcake topped with cream and cookie crumbs"></div>
    <p>Adipiscing elit. Maecenas eleifend, nunc non vehicula lacinia, odio massa porta lectus, blandit consectetur enim justo at metus. Vivamus eget dapibus nisliqua</p>
    <span class="more">Read More</span>
  </div>
  <div class="about-title" style="clear:both;padding-top:6px">Most Popular Cupcakes</div>
  <ul class="popular">
    <li><div class="pt t4" role="img" aria-label="Cookie dough cupcake"></div><div><h3>Cookie Dough Cupcakes with Crumbelle Frosting</h3><p>Porta lectus, blandit consectet</p></div></li>
    <li><div class="pt t3" role="img" aria-label="Peanut butter cup cupcake"></div><div><h3>Gourmet Rowan's Peanut Butter Cup Cupcakes</h3><p>Porta lectus, blandit consectet</p></div></li>
    <li><div class="pt t2" role="img" aria-label="Caramel apple cupcake"></div><div><h3>Caramel Apple Starmilk Cupcakes</h3><p>Porta lectus, blandit consectet</p></div></li>
    <li><div class="pt t1" role="img" aria-label="Brownie cupcake"></div><div><h3>Maribel's Brownie Cupcakes</h3><p>Adipiscing elit. Maecenas porta lectus, blandit consectet</p></div></li>
  </ul>
</aside>

<div class="abs footer-links">Home | Contribute | Advertise | Contact</div>
<div class="abs copyright">Copyright © 2014 Pagecraft Journal All Rights Reserved</div>
</body>
</html>
```